Business card design needed

I need a business card design for a dog walking, dog minding and dog training business. Please refer to my website for the basic company colours and fonts I'm after. Planning on a double sided card, so all information doesn't need to be on the 'front' side.
Cheers

Industry/Entity Type

Dog Training

Contact Information for Business Card

Meadow Paws - happy hounds
Rua 0498307164
meadowpawsdemo.com.au
-walking
-holiday stays
-onsite care
-training and behavioural consultations

```html
<!DOCTYPE html>
<html lang="en">
<head>
<meta charset="utf-8">
<title>Meadow Paws – Business Card</title>
<link rel="stylesheet" href="https://fonts.googleapis.com/css2?family=Arimo&family=Courier+Prime:wght@700&family=Open+Sans&family=Questrial&display=swap">
<style>
  :root {
    --card-bg: #ffffff;
    --ink: #111111;
    --brand-red: #e31b23;
    --band-text: #ffffff;
    --frame: #1a1a1a;
  }
  html, body {
    margin: 0;
    padding: 0;
    overflow: hidden;
    background: var(--card-bg);
  }
  .card {
    position: relative;
    width: 1200px;
    height: 693px;
    box-sizing: border-box;
    border: 2px solid var(--frame);
    background: var(--card-bg);
    overflow: hidden;
  }
  .brand-name {
    position: absolute;
    left: 43px;
    top: 42px;
    margin: 0;
    font-family: "Arimo", Arial, sans-serif;
    font-weight: 400;
    font-size: 82px;
    line-height: 1;
    letter-spacing: -1px;
    color: var(--brand-red);
    white-space: nowrap;
  }
  .tagline {
    position: absolute;
    right: 48px;
    top: 58px;
    margin: 0;
    font-family: "Questrial", "Century Gothic", sans-serif;
    font-size: 44px;
    line-height: 1;
    color: var(--ink);
    white-space: nowrap;
  }
  .contact-band {
    position: absolute;
    left: 43px;
    top: 222px;
    width: 1113px;
    height: 145px;
    background: var(--brand-red);
    color: var(--band-text);
    overflow: hidden;
  }
  .contact-name {
    position: absolute;
    left: 25px;
    top: 30px;
    font-family: "Courier Prime", "Courier New", monospace;
    font-weight: 700;
    font-size: 86px;
    line-height: 1;
  }
  .contact-phone,
  .contact-web {
    position: absolute;
    font-family: "Open Sans", Arial, sans-serif;
    line-height: 1;
    white-space: nowrap;
  }
  .contact-phone {
    left: 228px;
    top: 50px;
    font-size: 42px;
  }
  .contact-web {
    right: 36px;
    top: 52px;
    font-size: 38px;
  }
  .animal-lineup {
    position: absolute;
    left: 88px;
    top: 463px;
    width: 1013px;
    height: 170px;
  }
</style>
</head>
<body>
  <div class="card">
    <h1 class="brand-name">MEADOW PAWS</h1>
    <p class="tagline">happy hounds</p>

    <div class="contact-band">
      <span class="contact-name">Rua</span>
      <span class="contact-phone">0498 307 164</span>
      <span class="contact-web">meadowpawsdemo.com.au</span>
    </div>

    <svg class="animal-lineup" role="img" aria-label="Row of seated dogs and cats of many breeds facing forward" viewBox="0 0 1013 170" preserveAspectRatio="none">
      <defs>
        <linearGradient id="lineupTones" x1="0" y1="0" x2="1" y2="0">
          <stop offset="0" stop-color="#8a7d70"/>
          <stop offset="0.2" stop-color="#c9a98a"/>
          <stop offset="0.4" stop-color="#d9a46c"/>
          <stop offset="0.55" stop-color="#e8d2b8"/>
          <stop offset="0.7" stop-color="#c8b9a6"/>
          <stop offset="0.85" stop-color="#a8734a"/>
          <stop offset="1" stop-color="#9c8572"/>
        </linearGradient>
        <linearGradient id="lineupFade" x1="0" y1="0" x2="0" y2="1">
          <stop offset="0" stop-color="#fff" stop-opacity="0.55"/>
          <stop offset="0.35" stop-color="#fff" stop-opacity="0"/>
          <stop offset="1" stop-color="#fff" stop-opacity="0"/>
        </linearGradient>
      </defs>
      <rect x="0" y="0" width="1013" height="170" fill="url(#lineupTones)"/>
      <rect x="0" y="0" width="1013" height="170" fill="url(#lineupFade)"/>
    </svg>
  </div>
</body>
</html>
```